Marrow Aviation Group - "Coming Soon" Main Company Webpage

Design a main webpage that can be posted while a fully functional website is constructed. The design should be created to convey a sense of luxury and exclusivity. The main page should contain only one photo as the background. The photo I believe to show "luxury" and "Exclusivity" is listed as "Global Luxury Photo". I have included two other photos as well to aid in providing a variety of presentations.
The "Member TFPS" logo should appear somewhere on the main page but be less prevalent than the main company logo. "Coming Soon" should also appear to convey that a website is being constructed.
Tabs for the website:
- Aircraft Management
- Aircraft Sales
- Pilot Services
- Charter
- Flight Training

```html
<!DOCTYPE html>
<html lang="en">
<head>
<meta charset="utf-8">
<title>Marrow Aviation Group — Coming Soon</title>
<link rel="stylesheet" href="https://fonts.googleapis.com/css2?family=Russo+One&family=Space+Grotesk:wght@400;500;600;700&display=swap">
<style>
  :root {
    --brand-blue: #0b5cad;
    --ink: #111418;
    --white: #ffffff;
    --sky-light: #f1f2f3;
    --sky-mid: #d9dbdd;
    --sky-dark: #a9adb1;
  }
  * { box-sizing: border-box; margin: 0; padding: 0; }
  html, body { width: 1200px; height: 799px; overflow: hidden; }
  body { font-family: "Space Grotesk", sans-serif; color: var(--ink); }

  .page { position: relative; width: 1200px; height: 799px; overflow: hidden; }

  .hero-photo {
    position: absolute; inset: 0;
    background:
      radial-gradient(ellipse 55% 70% at 88% 70%, #f7f7f7 0%, #d6d8da 45%, transparent 75%),
      linear-gradient(160deg, var(--sky-light) 0%, var(--sky-mid) 45%, #c7cacd 75%, var(--sky-dark) 100%);
  }

  .site-header {
    position: absolute; left: 83px; right: 83px; top: 15px;
    display: flex; align-items: flex-start; justify-content: space-between;
  }
  .brand { color: var(--brand-blue); font-weight: 700; line-height: 1; margin-top: 17px; }
  .brand-name { font-size: 25px; letter-spacing: 1px; display: block; }
  .brand-sub { font-size: 12px; letter-spacing: 1.6px; display: block; margin-top: 3px; }

  .main-nav { display: flex; align-items: center; font-size: 10px; font-weight: 700; letter-spacing: 1.1px; margin-top: 24px; }
  .main-nav a { color: var(--ink); text-decoration: none; }
  .nav-active { display: flex; align-items: center; margin-right: 48px; }
  .nav-active a { border: 1px solid var(--ink); padding: 5px 7px; }
  .nav-arrow { width: 88px; height: 10px; }
  .main-nav .nav-item { margin-left: 47px; }
  .main-nav .nav-item:first-of-type { margin-left: 0; }

  .hero-content { position: absolute; left: 83px; top: 158px; width: 680px; }
  .hero-title {
    font-family: "Russo One", sans-serif; color: var(--brand-blue);
    font-size: 55px; letter-spacing: 1.5px; line-height: 1; font-weight: 400;
  }
  .hero-text { margin-top: 45px; font-size: 17px; line-height: 24.3px; letter-spacing: 0.9px; }
  .cta {
    display: inline-block; margin-top: 44px; background: var(--brand-blue); color: var(--white);
    font-size: 11.5px; font-weight: 700; letter-spacing: 1px; text-decoration: none;
    padding: 14px 18px; border-radius: 3px; width: 148px; text-align: center;
  }

  .membership { position: absolute; left: 83px; top: 711px; }
  .membership-label { font-size: 9px; display: block; margin-bottom: 1px; }
  .membership-name { font-size: 24px; font-weight: 500; letter-spacing: 2px; line-height: 1; display: block; }

  .menu-toggle { position: absolute; left: 1076px; top: 717px; width: 42px; height: 28px; }
</style>
</head>
<body>
<div class="page">
  <div class="hero-photo" role="img" aria-label="Private jet fuselage, wing and rear engine under an overcast grey sky"></div>

  <header class="site-header">
    <div class="brand">
      <span class="brand-name">MARROW</span>
      <span class="brand-sub">AVIATION GROUP</span>
    </div>
    <nav class="main-nav">
      <span class="nav-active">
        <a href="#">AIRCRAFT SALES</a>
        <svg class="nav-arrow" viewBox="0 0 88 10"><line x1="0" y1="5" x2="82" y2="5" stroke="#111418" stroke-width="1"/><polygon points="76,1 88,5 76,9" fill="#111418"/></svg>
      </span>
      <a class="nav-item" href="#">AIRCRAFT MANAGEMENT ˅</a>
      <a class="nav-item" href="#">PILOT SERVICES</a>
      <a class="nav-item" href="#">CHARTER</a>
      <a class="nav-item" href="#">FLIGHT TRAINING</a>
    </nav>
  </header>

  <main class="hero-content">
    <h1 class="hero-title">COMING SOON</h1>
    <p class="hero-text">Lorem Ipsum Is Simply Dummy Text Of The Printing And<br>Typesetting Industry. Lorem Ipsum Has Been The Industry’s<br>Standard Dummy Text Ever Since The 1500s, When An Unknown<br>Printer Took A Galley Of Type And Scrambled It To Make A<br>Type Specimen Book. It Has Survived Not Only Five Centuries,<br>But Also The Leap Into Electronic Typesetting, Remaining Essentially<br>Unchanged. It Was Popularised In The 1960s With The Release Of<br>Lettrafix Sheets Containing Lorem Ipsum Passages, And More Recently<br>With Desktop Publishing Software Like Quill PageSetter Including<br>Versions Of Lorem Ipsum.</p>
    <a class="cta" href="#">SCHEDULE A CALL</a>
  </main>

  <div class="membership">
    <span class="membership-label">member of</span>
    <span class="membership-name">TFPS</span>
  </div>

  <svg class="menu-toggle" viewBox="0 0 42 28" aria-label="Menu">
    <line x1="0" y1="1.5" x2="42" y2="1.5" stroke="#111418" stroke-width="2.5"/>
    <line x1="18" y1="14" x2="42" y2="14" stroke="#111418" stroke-width="2.5"/>
    <line x1="0" y1="26.5" x2="42" y2="26.5" stroke="#111418" stroke-width="2.5"/>
  </svg>
</div>
</body>
</html>
```